New Business Card for Casual Beachfront Cafe

Quirky Beachfront Cafe at Moana, South Australia needs a DOUBLE SIDED business card to print on PrintHarbor.

Target Market(s)

Business Cards sit on the counter for Guests to take with them. Please view our website www.saltreefcafe.com.au to get a feel for the Cafe. You may also view our Instagram at @saltreefcafe

Industry/Entity Type

Cafe / Restaurant

Contact Information for Business Card

Information equivalent to: Breakfast, Lunch, Dinner, Coffee, Takeaway / 117 Parade Moana SA 5169 / Menu & Opening Hours: www.saltreefcafe.com.au / ph (08) 8461 9273

Requirements
Must have
• Information equivalent to: Breakfast, Lunch, Dinner, Coffee, Takeaway / 117 Parade Moana SA 5169 / Menu & Opening Hours: www.saltreefcafe.com.au / ph (08) 8461 9273
Nice to have
• Potentially some of our trademark colours (Cafe can be searched via Seekly)
Should not have
• Must NOT have image of the building. May have the logo provided on one side but not necessarily, depending on how you wish to design the card

```html
<!DOCTYPE html>
<html lang="en">
<head>
<meta charset="utf-8">
<title>Salt Reef Cafe – Business Card</title>
<link rel="stylesheet" href="https://fonts.googleapis.com/css2?family=Roboto:wght@400;500;700&display=swap">
<style>
  :root {
    --backdrop: #2c2c2c;
    --paper: #f1f1f1;
    --paper-shade: #e2e2e2;
    --navy: #1c3b78;
    --ink: #222222;
    --rust: #a8491a;
    --lemon: #dede12;
    --sky: #1b8fd2;
  }
  * { box-sizing: border-box; margin: 0; padding: 0; }
  html, body {
    width: 1200px; height: 1138px; overflow: hidden;
    background: var(--backdrop);
    font-family: "Roboto", Arial, sans-serif;
  }
  .card {
    position: absolute;
    width: 620px; height: 375px;
    border-radius: 16px;
    overflow: hidden;
    background: linear-gradient(180deg, var(--paper) 0%, #f6f6f6 45%, var(--paper-shade) 100%);
  }
  .card--front { left: 274px; top: 186px; }
  .card--back  { left: 276px; top: 608px; }

  .colour-band {
    position: absolute; left: 0; right: 0; bottom: 0; height: 10px;
    display: flex;
  }
  .colour-band span { flex: 1; }
  .colour-band .navy { background: var(--navy); }
  .colour-band .lemon { background: var(--lemon); }
  .colour-band .rust { background: var(--rust); }

  .brand-name {
    position: absolute;
    display: flex; flex-direction: column; align-items: center; justify-content: center;
    color: var(--navy);
    font-weight: 700;
    line-height: 1;
    text-transform: uppercase;
    letter-spacing: 1px;
  }
  .card--front .brand-name { left: 78px; top: 103px; width: 272px; height: 141px; }
  .card--back .brand-name { left: 185px; top: 73px; width: 249px; height: 129px; }
  .brand-name .top { font-size: 40px; }
  .brand-name .bottom { font-size: 54px; margin-top: 6px; }
  .card--back .brand-name .top { font-size: 37px; }
  .card--back .brand-name .bottom { font-size: 50px; }

  .services {
    position: absolute; left: 412px; top: 102px;
    list-style: none;
  }
  .services li {
    display: flex; align-items: center;
    height: 30px;
    color: var(--navy);
    font-weight: 700;
    font-size: 19px;
    letter-spacing: 0.2px;
  }
  .services svg { width: 16px; height: 16px; margin-right: 10px; }

  .web-line {
    position: absolute; left: 0; right: 0; top: 327px;
    display: flex; align-items: center; justify-content: center; gap: 24px;
    color: var(--ink); font-size: 16px;
  }
  .web-line .rule {
    width: 70px; height: 3px;
    background: var(--sky);
    clip-path: polygon(0 50%, 100% 0, 100% 100%);
  }
  .web-line .rule--right { clip-path: polygon(0 0, 100% 50%, 0 100%); }

  .call-now {
    position: absolute; left: 0; right: 0; top: 266px;
    text-align: center; font-size: 22px; color: var(--ink);
  }
  .call-now strong { font-weight: 700; }

  .contact-line {
    position: absolute; left: 0; right: 0; top: 310px;
    display: flex; align-items: center; justify-content: center;
    font-size: 16px; color: var(--ink);
  }
  .contact-line svg { width: 16px; height: 16px; margin-right: 10px; }
  .contact-line .address { margin-right: 20px; }
  .contact-line .item { display: flex; align-items: center; }
</style>
</head>
<body>

<section class="card card--front">
  <div class="brand-name"><span class="top">Salt Reef</span><span class="bottom">Cafe</span></div>

  <ul class="services">
    <li><svg viewBox="0 0 16 16" aria-hidden="true"><path d="M2 8h10M8 3l5 5-5 5" fill="none" stroke="#a8491a" stroke-width="2.2" stroke-linecap="round" stroke-linejoin="round"/></svg>BREAKFAST</li>
    <li><svg viewBox="0 0 16 16" aria-hidden="true"><path d="M2 8h10M8 3l5 5-5 5" fill="none" stroke="#a8491a" stroke-width="2.2" stroke-linecap="round" stroke-linejoin="round"/></svg>LUNCH</li>
    <li><svg viewBox="0 0 16 16" aria-hidden="true"><path d="M2 8h10M8 3l5 5-5 5" fill="none" stroke="#a8491a" stroke-width="2.2" stroke-linecap="round" stroke-linejoin="round"/></svg>DINNER</li>
    <li><svg viewBox="0 0 16 16" aria-hidden="true"><path d="M2 8h10M8 3l5 5-5 5" fill="none" stroke="#a8491a" stroke-width="2.2" stroke-linecap="round" stroke-linejoin="round"/></svg>COFFEE</li>
    <li><svg viewBox="0 0 16 16" aria-hidden="true"><path d="M2 8h10M8 3l5 5-5 5" fill="none" stroke="#a8491a" stroke-width="2.2" stroke-linecap="round" stroke-linejoin="round"/></svg>TAKEAWAY</li>
  </ul>

  <div class="web-line">
    <span class="rule"></span>
    <span>www.saltreefcafe.com.au</span>
    <span class="rule rule--right"></span>
  </div>

  <div class="colour-band"><span class="navy"></span><span class="lemon"></span><span class="rust"></span></div>
</section>

<section class="card card--back">
  <div class="brand-name"><span class="top">Salt Reef</span><span class="bottom">Cafe</span></div>

  <p class="call-now">Call Now: <strong>(08) 8461 9273</strong></p>

  <div class="contact-line">
    <span class="item address">
      <svg viewBox="0 0 16 16" aria-hidden="true"><path d="M8 15s5-5.2 5-9A5 5 0 0 0 3 6c0 3.8 5 9 5 9z" fill="#a8491a"/><circle cx="8" cy="6" r="2" fill="#f1f1f1"/></svg>
      117 Parade Moana SA 5169
    </span>
    <span class="item">
      <svg viewBox="0 0 16 16" aria-hidden="true"><g fill="none" stroke="#a8491a" stroke-width="1.4"><circle cx="8" cy="8" r="6"/><ellipse cx="8" cy="8" rx="2.6" ry="6"/><path d="M2 8h12M3 5h10M3 11h10"/></g></svg>
      www.saltreefcafe.com.au
    </span>
  </div>

  <div class="colour-band"><span class="navy"></span><span class="lemon"></span><span class="rust"></span></div>
</section>

</body>
</html>
```